Keystone Facility Partners Business card

We wish to have a professional Business card to present to large Corporate CEO's ASAP.

Our web site helps explain our business www.keystonefp.org

Keystone Facility Partners was established after we discovered how difficult it is to organise outsourced services while heading up a business or company.

We act as a facilitator for businesses who don't have the desire, expertise or recourses to manage their own systems and meet all their requirements.

We provide an all in one facility management solution for all types of businesses. We manage schedules, contractors and costs on behalf of businesses and their needs and wants.

Having an extensive network ensures we are able to connect businesses with the right service providers.

Target Market(s)

Company CEO

Industry/Entity Type

Business

Font styles to use
Sans Serif

Colors
33a6d7
f9fdfe
0355a3

Requirements
Must have
• professional design
Nice to have
• colours to match logo

```html
<!DOCTYPE html>
<html lang="en">
<head>
<meta charset="utf-8">
<title>Keystone Facility Partners – Business Card</title>
<link rel="stylesheet" href="https://fonts.googleapis.com/css2?family=Lato:wght@300;400;700&display=swap">
<style>
  :root {
    --sky: #33a6d7;
    --sky-light: #3fb6e6;
    --sky-deep: #1f97c9;
    --paper: #f9fdfe;
    --paper-shade: #e9eded;
    --navy: #0355a3;
    --ink: #1c2430;
    --name-soft: #bfe6f5;
    --backdrop: #2c2c2e;
  }
  * { box-sizing: border-box; margin: 0; padding: 0; }
  html, body {
    width: 1200px; height: 997px; overflow: hidden;
    background: var(--backdrop);
    font-family: "Lato", Arial, sans-serif;
  }
  .canvas { position: relative; width: 1200px; height: 997px; }

  .card {
    position: absolute;
    width: 640px; height: 366px;
    border-radius: 26px;
    overflow: hidden;
    box-shadow: 0 18px 40px rgba(0,0,0,.45);
  }

  /* Back of card */
  .card-back {
    left: 70px; top: 90px;
    background: linear-gradient(150deg, var(--sky-light), var(--sky) 55%, var(--sky-deep));
  }
  .card-back .back-brand {
    position: absolute; right: 40px; bottom: 70px;
    text-align: left;
  }
  .back-tagline {
    font-size: 13px; font-weight: 400; letter-spacing: .5px;
    color: var(--ink); margin-bottom: 4px;
  }
  .back-name {
    font-size: 21px; font-weight: 700; letter-spacing: 1px;
    color: var(--ink); text-transform: uppercase;
  }

  /* Front of card */
  .card-front {
    left: 490px; top: 520px;
    background: linear-gradient(180deg, var(--paper), var(--paper-shade) 52%);
  }
  .front-band {
    position: absolute; left: 0; right: 0; top: 200px; bottom: 0;
    background: linear-gradient(180deg, var(--sky-light), var(--sky) 60%, var(--sky-deep));
  }
  .band-stripes {
    position: absolute; left: 0; right: 0; top: 180px; height: 20px;
    background: var(--sky);
  }
  .band-stripes::before, .band-stripes::after {
    content: ""; position: absolute; left: 0; right: 0; height: 3px;
    background: var(--paper);
  }
  .band-stripes::before { top: 5px; }
  .band-stripes::after { top: 12px; }

  .front-brand {
    position: absolute; left: 150px; top: 70px;
    display: flex; align-items: center; gap: 14px;
  }
  .brand-dot {
    width: 34px; height: 34px; border-radius: 50%;
    background: var(--navy);
  }
  .brand-name {
    font-size: 24px; font-weight: 700; letter-spacing: 1.5px;
    color: var(--navy); text-transform: uppercase;
  }

  .holder-name {
    position: absolute; left: 40px; bottom: 56px;
    font-size: 26px; font-weight: 400; letter-spacing: 1px;
    text-transform: uppercase; color: var(--paper);
  }
  .holder-name .first { color: var(--name-soft); }

  .contact-list {
    position: absolute; left: 380px; top: 222px;
    list-style: none;
  }
  .contact-list li {
    display: flex; align-items: center; gap: 10px;
    height: 32px;
    font-size: 15px; color: var(--paper);
  }
  .contact-icon { width: 22px; height: 22px; flex: none; }
</style>
</head>
<body>
<main class="canvas">

  <section class="card card-back" aria-label="Business card back">
    <div class="back-brand">
      <p class="back-tagline">FACILITIES MANAGEMENT SOLUTIONS</p>
      <p class="back-name">Keystone Facility Partners</p>
    </div>
  </section>

  <section class="card card-front" aria-label="Business card front">
    <div class="front-band"></div>
    <div class="band-stripes"></div>

    <div class="front-brand">
      <span class="brand-dot"></span>
      <span class="brand-name">Keystone Facility Partners</span>
    </div>

    <p class="holder-name"><span class="first">Daniel</span> Whitford</p>

    <ul class="contact-list">
      <li>
        <svg class="contact-icon" viewBox="0 0 22 22" aria-hidden="true">
          <rect x="1" y="1" width="20" height="20" rx="3" fill="none" stroke="#f9fdfe" stroke-width="1.6"/>
          <path d="M7 5.5c-1 .6-1.6 1.8-1 3.4 1 2.6 3.5 5.4 6.3 6.9 1.4.7 2.6.3 3.3-.7l-2.2-2.1-1.6 1c-1.4-.8-2.7-2.2-3.4-3.7l1-1.5z" fill="#f9fdfe"/>
        </svg>
        0400 127 958
      </li>
      <li>
        <svg class="contact-icon" viewBox="0 0 22 22" aria-hidden="true">
          <rect x="1" y="1" width="20" height="20" rx="3" fill="none" stroke="#f9fdfe" stroke-width="1.6"/>
          <rect x="5" y="9" width="7" height="4" rx="2" transform="rotate(-45 8.5 11)" fill="none" stroke="#f9fdfe" stroke-width="1.6"/>
          <rect x="10" y="9" width="7" height="4" rx="2" transform="rotate(-45 13.5 11)" fill="none" stroke="#f9fdfe" stroke-width="1.6"/>
        </svg>
        www.keystonefp.org
      </li>
      <li>
        <svg class="contact-icon" viewBox="0 0 22 22" aria-hidden="true">
          <rect x="1" y="1" width="20" height="20" rx="3" fill="none" stroke="#f9fdfe" stroke-width="1.6"/>
          <rect x="5" y="7" width="12" height="8" fill="none" stroke="#f9fdfe" stroke-width="1.4"/>
          <path d="M5 7l6 5 6-5" fill="none" stroke="#f9fdfe" stroke-width="1.4"/>
        </svg>
        daniel@keystonefp.org
      </li>
    </ul>
  </section>

</main>
</body>
</html>
```